Tall Harbor Business Card

We are a Video Production and Video Equipment Rental company specialising in the supply of state of the art Video Technology and Services for the Live Entertainment, Television and Corporate Business Theatre markets. (in Sydney, Australia) www.tallharbor-media.example

Industry/Entity Type

Business

Contact Information for Business Card

name, position, email, website, address, logo
Example attached of the information we need - doesn't necessarily have to look the same

Font styles to use
Other font styles liked:
• Tall Harbor logo font is GOTHAM

Colors
ea1f27

Requirements
Nice to have
• either matt black or shiny black cards -
raised logo

```html
<!DOCTYPE html>
<html lang="en">
<head>
<meta charset="utf-8">
<title>Tall Harbor Business Card</title>
<link rel="stylesheet" href="https://fonts.googleapis.com/css2?family=Montserrat:wght@500&family=Oswald:wght@400;500&display=swap">
<style>
  :root {
    --brand-red: #ea1f27;
    --card-black: #000000;
    --card-white: #ffffff;
    --ink: #111111;
    --backdrop: #2a2a2a;
  }
  * { box-sizing: border-box; margin: 0; padding: 0; }
  html, body {
    width: 1200px;
    height: 800px;
    overflow: hidden;
    background: var(--backdrop);
  }
  .stage {
    width: 1200px;
    height: 800px;
    display: flex;
    align-items: center;
    justify-content: center;
  }
  .business-card {
    width: 420px;
    height: 680px;
    display: flex;
    flex-direction: column;
    box-shadow: 0 6px 24px rgba(0,0,0,0.45);
  }
  .card-front {
    height: 413px;
    background: var(--card-black);
    color: var(--card-white);
    position: relative;
  }
  .brand-name {
    position: absolute;
    top: 128px;
    left: 0;
    right: 0;
    text-align: center;
    font-family: "Montserrat", sans-serif;
    font-weight: 500;
    font-size: 34px;
    letter-spacing: 1px;
    color: var(--card-white);
  }
  .services-line {
    position: absolute;
    top: 222px;
    left: 0;
    right: 0;
    text-align: center;
    font-family: "Oswald", sans-serif;
    font-weight: 400;
    font-size: 11px;
    letter-spacing: 0.3px;
    color: var(--card-white);
  }
  .person {
    position: absolute;
    right: 34px;
    top: 326px;
    text-align: right;
    font-family: "Oswald", sans-serif;
  }
  .person-name {
    font-weight: 400;
    font-size: 21px;
    letter-spacing: 1.5px;
    color: var(--brand-red);
    word-spacing: 4px;
  }
  .person-role {
    margin-top: 6px;
    font-size: 12px;
    letter-spacing: 0.4px;
    color: var(--card-white);
  }
  .card-contact {
    flex: 1;
    background: var(--card-white);
    padding: 30px 0 0 92px;
    font-family: "Oswald", sans-serif;
    font-weight: 500;
    color: var(--ink);
  }
  .contact-row {
    display: flex;
    align-items: flex-start;
    margin-bottom: 20px;
  }
  .contact-icon {
    width: 34px;
    height: 34px;
    flex: none;
    margin-right: 20px;
    margin-top: -4px;
  }
  .contact-text {
    font-size: 16px;
    letter-spacing: 0.8px;
    line-height: 1.2;
  }
  .contact-text .accent { color: var(--brand-red); }
  .address-row .contact-text { line-height: 1.25; }
</style>
</head>
<body>
<main class="stage">
  <article class="business-card">
    <section class="card-front">
      <h1 class="brand-name">TALL HARBOR</h1>
      <p class="services-line">VIDEO SOLUTIONS - LED SCREENS - CAMERA SYSTEMS - PROJECTION</p>
      <div class="person">
        <p class="person-name">DANA WHITLOW</p>
        <p class="person-role">MANAGING DIRECTOR</p>
      </div>
    </section>
    <section class="card-contact">
      <div class="contact-row web-row">
        <svg class="contact-icon" viewBox="0 0 34 34" aria-hidden="true">
          <g fill="none" stroke="#ea1f27" stroke-width="1.8">
            <circle cx="17" cy="17" r="13"/>
            <ellipse cx="17" cy="17" rx="6" ry="13"/>
            <line x1="4" y1="17" x2="30" y2="17"/>
            <line x1="6" y1="10.5" x2="28" y2="10.5"/>
            <line x1="6" y1="23.5" x2="28" y2="23.5"/>
          </g>
        </svg>
        <p class="contact-text">WWW.<span class="accent">TALLHARBOR-MEDIA</span>.EXAMPLE</p>
      </div>
      <div class="contact-row mail-row">
        <svg class="contact-icon" viewBox="0 0 34 34" aria-hidden="true">
          <rect x="3" y="8" width="28" height="19" fill="#ea1f27"/>
          <polyline points="3,8 17,19 31,8" fill="none" stroke="#ffffff" stroke-width="1.8"/>
        </svg>
        <p class="contact-text">DANA@TALLHARBOR-MEDIA.EXAMPLE</p>
      </div>
      <div class="contact-row address-row">
        <svg class="contact-icon" viewBox="0 0 34 34" aria-hidden="true">
          <path d="M17 3 C10.5 3 7 7.5 7 12.5 C7 19 17 33 17 33 C17 33 27 19 27 12.5 C27 7.5 23.5 3 17 3 Z" fill="#ea1f27"/>
          <circle cx="17" cy="12.5" r="3.6" fill="#ffffff"/>
        </svg>
        <p class="contact-text">12 KEEL STREET<br>MARLOW NSW 2100<br>AUSTRALIA.</p>
      </div>
    </section>
  </article>
</main>
</body>
</html>
```